Halvard Atelier Business cards

Design our business cards and eventually a logo. The company is based in Paris, its activity is the retailing via internet of luxury home furniture (like Vambrelli, Bercusa, tarvoni...) Our clients are international andwith a high sense of aesthetics. The design shall communicate wealth and trust with a high quality and aesthetic sense, pure lines Company Name is Halvard AtelierExplanation of the name: usually people who wants to buy furniture usually go in a showroom. Today they go in showroom to test the furniture and they search for the price on internet, which is a "Halvard atelier".We will not be a e-commerce site. Our site will be (another project) a presentation site which purpose is to reach qualified prospects. Then everything will be handled by phone, meeting etc.The business card must be professional as we will negotiate with many luxury brands, opportunity to represent them on our site, prices etc.As far as the color are concerned mostly black and whithe or grey. The font of the Halvard Atelier name shall have some impact.

Target Market(s)

High-end furniture and buyers of luxury goods, international customers, mostly women who handle such projects.
We also deal with professional buyers (hotels as an example) and luxury brands

Contact Information for Business Card

standard format 85x55, lanscape card, square corners will be printed on thick high quality paper (300 or 350g)

Font styles to use
Sans Serif

Colors

Designer to choose colors to be used in the design.

Requirements
Must have
• Must be white, as the paper will be high quality, the paper will enhance the card.
• Name of the brand Halvard atelier (with specific font which make it very nice looking and catch the attention. similar to Calibri or Calibri
• Name of person (will give you the name later (4 names and position)
• the position of the person
• Mobile phone, e-mail, Physical address 27, rue Fenouillard, 75005 Paris, France (courrier only) our web site www.halvardatelier.fr
• The card must be simple and class
Nice to have
• Font of the address is smaller than the rest,
• Calibri font or similar on recto side with the name of the company which may look similar to the picture inserted in the brief.
• The grey color in the picture inserted is ok for us
Should not have
• Any parallel lines which represent the name of the company
• Any heavy design If you go on internet sites which present the furniture all designs are pure lines and high quality craftsmanship. To have an idea of our targetted client or brand we will be in touch: https://www.casavelumi.it/projects/
• Note that the picture added below is what we use, now as mail signature, up to you to have a better design etc.

```html
<!DOCTYPE html>
<html lang="fr">
<head>
<meta charset="utf-8">
<title>Halvard Atelier — Business Cards</title>
<link rel="stylesheet" href="https://fonts.googleapis.com/css2?family=Montserrat:ital,wght@0,400;0,500;1,400&family=Oswald:wght@300&display=swap">
<style>
  :root {
    --stage: #58595b;
    --paper: #ffffff;
    --ink: #4b4b4d;
    --ink-soft: #5a5a5c;
    --rule: #c4c4c6;
    --rule-dark: #8a8a8c;
    --on-dark: #ffffff;
  }
  * { box-sizing: border-box; margin: 0; padding: 0; }
  html, body {
    width: 1200px; height: 566px; overflow: hidden;
    background: var(--stage);
  }
  .stage { position: relative; width: 1200px; height: 566px; }

  .option-label {
    position: absolute; top: 86px; width: 200px; margin-left: -100px;
    text-align: center; color: var(--paper);
    font-family: "Oswald", sans-serif; font-weight: 300;
    font-size: 26px; letter-spacing: 0.5px;
    -webkit-text-stroke: 0.9px var(--paper);
  }
  .option-label--one { left: 324px; }
  .option-label--two { left: 894px; }

  .card {
    position: absolute; top: 136px; width: 522px; height: 350px;
    background: var(--paper); color: var(--ink);
    font-family: "Montserrat", sans-serif;
  }
  .card--light { left: 58px; }
  .card--dark { left: 619px; }
  .card__panel {
    position: absolute; left: 18px; top: 18px; width: 486px; height: 314px;
    background: var(--ink);
  }
  .card--dark .card__content { color: var(--on-dark); }
  .card__content { position: absolute; inset: 0; }

  .person { position: absolute; right: 43px; top: 57px; text-align: right; }
  .person__name { font-size: 24px; font-weight: 400; line-height: 1; letter-spacing: 0.2px; }
  .person__role { font-size: 14.5px; font-style: italic; line-height: 1; margin-top: 6px; opacity: 0.95; }

  .brand { position: absolute; left: 44px; top: 147px; }
  .brand__name {
    font-size: 27px; font-weight: 500; line-height: 1;
    letter-spacing: 1.2px; text-transform: uppercase;
  }
  .brand__tagline {
    font-family: "Oswald", sans-serif; font-weight: 300;
    font-size: 13.5px; line-height: 1; margin-top: 5px; letter-spacing: 0.1px;
  }

  .divider { position: absolute; left: 0; right: 0; top: 224px; height: 1px; background: var(--rule); }
  .card--dark .divider { left: 18px; right: 18px; background: var(--rule-dark); }

  .contact {
    position: absolute; text-align: right;
    font-size: 11.5px; line-height: 1; letter-spacing: 0.4px;
  }
  .contact--web { right: 330px; top: 248px; }
  .contact--mail { right: 330px; top: 281px; }
  .contact--phone { right: 73px; top: 248px; }
  .contact--address { right: 73px; top: 276px; font-size: 9.8px; line-height: 12.5px; }

  .icon { position: absolute; width: 22px; height: 22px; }
  .icon--web { left: 200px; top: 242px; }
  .icon--mail { left: 200px; top: 275px; }
  .icon--phone { left: 457px; top: 242px; }
  .icon--pin { left: 457px; top: 274px; }
  .icon__disc { fill: var(--ink); }
  .icon__glyph { fill: var(--paper); }
  .card--dark .icon__disc { fill: none; }
  .card--dark .icon__glyph { fill: var(--on-dark); }
</style>
</head>
<body>
<main class="stage">
  <h2 class="option-label option-label--one">OPTION 1</h2>
  <h2 class="option-label option-label--two">OPTION 2</h2>

  <!-- Light card -->
  <section class="card card--light">
    <div class="card__content">
      <div class="person">
        <p class="person__name">MATHIS DEROUET</p>
        <p class="person__role">Président &amp; Co-Founder</p>
      </div>
      <div class="brand">
        <p class="brand__name">Halvard Atelier</p>
        <p class="brand__tagline">THE BEST TEAM TO PROVIDE YOU WITH HIGH-END FURNITURE</p>
      </div>
      <div class="divider"></div>

      <p class="contact contact--web">www.halvardatelier.fr</p>
      <svg class="icon icon--web" viewBox="0 0 22 22"><circle class="icon__disc" cx="11" cy="11" r="11"/><path class="icon__glyph" d="M11 4.5a6.5 6.5 0 1 0 0 13a6.5 6.5 0 0 0 0-13zm-1 2.2c.6.7.2 1.6-.6 1.9c-.9.3-1.4 1-.9 1.8c.6.8 1.7.4 2.3 1.2c.5.7-.2 1.6.1 2.5c.2.7.1 1.6-.4 2.1A5.2 5.2 0 0 1 7 7.3c1-.5 2-.7 3-.6zm3.3.5a5.2 5.2 0 0 1 2.9 4.6c-.6-.3-1.2-.9-1.9-.6c-.8.4-1.4-.3-1.6-1c-.3-1 .9-1.2.9-2.1c0-.4-.2-.7-.3-.9z"/></svg>

      <p class="contact contact--mail">@halvardatelier.fr</p>
      <svg class="icon icon--mail" viewBox="0 0 22 22"><circle class="icon__disc" cx="11" cy="11" r="11"/><path class="icon__glyph" d="M5 7h12v8H5zm1 .8l5 4 5-4v-.1H6zm0 1.3v5.2l3.2-2.6zm10 0l-3.2 2.6l3.2 2.6zM9.9 12.2L6.6 14.9h8.8l-3.3-2.7l-1.1.9z"/></svg>

      <p class="contact contact--phone">+33612847390</p>
      <svg class="icon icon--phone" viewBox="0 0 22 22"><circle class="icon__disc" cx="11" cy="11" r="11"/><path class="icon__glyph" d="M8.3 4.8h5.4c.6 0 1 .4 1 1v10.4c0 .6-.4 1-1 1H8.3c-.6 0-1-.4-1-1V5.8c0-.6.4-1 1-1zm.3 1.6v8.5h4.8V6.4zm2.4 9.2a.6.6 0 1 0 0 .01z"/></svg>

      <p class="contact contact--address">27, rue Fenouillard, 75005 Paris, France<br>(courrier only)</p>
      <svg class="icon icon--pin" viewBox="0 0 22 22"><circle class="icon__disc" cx="11" cy="11" r="11"/><path class="icon__glyph" d="M11 4.3a4.4 4.4 0 0 0-4.4 4.4c0 3.1 4.4 7.8 4.4 7.8s4.4-4.7 4.4-7.8A4.4 4.4 0 0 0 11 4.3zm0 2.6a1.8 1.8 0 1 1 0 3.6a1.8 1.8 0 0 1 0-3.6zM8 16.9h6v1H8z"/></svg>
    </div>
  </section>

  <!-- Dark card -->
  <section class="card card--dark">
    <div class="card__panel"></div>
    <div class="card__content">
      <div class="person">
        <p class="person__name">MATHIS DEROUET</p>
        <p class="person__role">Président &amp; Co-Founder</p>
      </div>
      <div class="brand">
        <p class="brand__name">Halvard Atelier</p>
        <p class="brand__tagline">THE BEST TEAM TO PROVIDE YOU WITH HIGH-END FURNITURE</p>
      </div>
      <div class="divider"></div>

      <p class="contact contact--web">www.halvardatelier.fr</p>
      <svg class="icon icon--web" viewBox="0 0 22 22"><circle class="icon__disc" cx="11" cy="11" r="11"/><path class="icon__glyph" d="M11 4.5a6.5 6.5 0 1 0 0 13a6.5 6.5 0 0 0 0-13zm-1 2.2c.6.7.2 1.6-.6 1.9c-.9.3-1.4 1-.9 1.8c.6.8 1.7.4 2.3 1.2c.5.7-.2 1.6.1 2.5c.2.7.1 1.6-.4 2.1A5.2 5.2 0 0 1 7 7.3c1-.5 2-.7 3-.6zm3.3.5a5.2 5.2 0 0 1 2.9 4.6c-.6-.3-1.2-.9-1.9-.6c-.8.4-1.4-.3-1.600-1c-.3-1 .9-1.2.9-2.1c0-.4-.2-.7-.3-.9z"/></svg>

      <p class="contact contact--mail">@halvardatelier.fr</p>
      <svg class="icon icon--mail" viewBox="0 0 22 22"><circle class="icon__disc" cx="11" cy="11" r="11"/><path class="icon__glyph" d="M5 7h12v8H5zm1 .8l5 4 5-4v-.1H6zm0 1.3v5.2l3.2-2.6zm10 0l-3.2 2.6l3.2 2.6zM9.9 12.2L6.6 14.9h8.8l-3.3-2.7l-1.1.9z"/></svg>

      <p class="contact contact--phone">+33612847390</p>
      <svg class="icon icon--phone" viewBox="0 0 22 22"><circle class="icon__disc" cx="11" cy="11" r="11"/><path class="icon__glyph" d="M8.3 4.8h5.4c.6 0 1 .4 1 1v10.4c0 .6-.4 1-1 1H8.3c-.6 0-1-.4-1-1V5.8c0-.6.4-1 1-1zm.3 1.6v8.5h4.8V6.4zm2.4 9.2a.6.6 0 1 0 0 .01z"/></svg>

      <p class="contact contact--address">27, rue Fenouillard, 75005 Paris, France<br>(courrier only)</p>
      <svg class="icon icon--pin" viewBox="0 0 22 22"><circle class="icon__disc" cx="11" cy="11" r="11"/><path class="icon__glyph" d="M11 4.3a4.4 4.4 0 0 0-4.4 4.4c0 3.1 4.4 7.8 4.4 7.8s4.4-4.7 4.4-7.8A4.4 4.4 0 0 0 11 4.3zm0 2.6a1.8 1.8 0 1 1 0 3.6a1.8 1.8 0 0 1 0-3.6zM8 16.9h6v1H8z"/></svg>
    </div>
  </section>
</main>
</body>
</html>
```